SEAFOOD PACKAGING (Products for consumer)

We are looking to create packaging for various seafood products such as octopus and squid. We plan to sell our products in upscale supermarkets.

We are specializing in cut octopus this time.

Please include our company logo. Also, please leave a transparent area so that customers can see the product inside.
Updates

We want to show what is inside, so a picture of the octopus is not required. We need something simple and sophisticated.

Target Market(s)

upscale store in US and ASIA

Industry/Entity Type

Fisheries dealer

Requirements
Must have
• Please include the attached logo,Blue one is preferred.Please leave a transparent part so that the contents of the product can be seen by the consumer.1. product name on packaging →CUT OCTOPUS,TAKO SASHIMI,Highest quality,Top quality etc... 3. What text information should be on the packaging →(It may be edited, but this is the image) The raw materials are caught in a very clean environment and processed in a modern factory with ZEK certification. We are committed to additive-free products. 4. Packing size(cm/inch)→it will be about 19cm*22cm. 5. what kind of packaging do you use →PP or PA 6. dll →ai,jag
Nice to have
• https://quillmora.example/shots/4829174-Velka-Reef We need something simple and sophisticated like this one.
Should not have
• We want to show what is inside, so a picture of the octopus is not required. We need something simple and sophisticated.

```html
<!DOCTYPE html>
<html lang="en">
<head>
<meta charset="UTF-8">
<title>Marenji Cut Octopus Packaging</title>
<link href="https://fonts.googleapis.com/css2?family=Montserrat:wght@400;500;600;700&family=EB+Garamond:ital@1&display=swap" rel="stylesheet">
<style>
  :root {
    --backdrop: #8a8a8a;
    --film-top: #ececec;
    --film-bottom: #d6d6d6;
    --seal-line: #cfcfcf;
    --label: #f7f7f7;
    --ink: #111118;
    --body-ink: #333340;
    --rule: #2e3048;
    --brand-red: #e5202a;
    --sea-blue: #1a9ad9;
  }
  * { margin: 0; padding: 0; box-sizing: border-box; }
  html, body { width: 1200px; height: 997px; overflow: hidden; }
  body { background: var(--backdrop); font-family: "Montserrat", sans-serif; color: var(--ink); }
  .canvas { position: relative; width: 1200px; height: 997px; overflow: hidden; }

  .pouch {
    position: absolute; left: 276px; top: 173px; width: 561px; height: 659px;
    background: linear-gradient(180deg, var(--film-top), var(--film-bottom));
  }
  .pouch__seal {
    position: absolute; left: 0; right: 0; height: 7px;
    background: repeating-linear-gradient(180deg, #f2f2f2 0 2px, var(--seal-line) 2px 3px);
  }
  .pouch__seal--top { top: 0; }
  .pouch__seal--bottom { bottom: 0; }

  .label {
    position: absolute; left: 139px; top: 7px; width: 286px; height: 645px;
    background: var(--label); overflow: hidden;
  }

  .brand {
    position: absolute; top: 62px; left: 0; width: 100%;
    display: flex; flex-direction: column; align-items: center; gap: 38px;
  }
  .brand__dot { width: 34px; height: 34px; border-radius: 50%; background: var(--brand-red); }
  .brand__name { font-weight: 700; font-size: 32px; letter-spacing: 4px; color: var(--brand-red); line-height: 1; }

  .product-name {
    position: absolute; top: 209px; left: 0; width: 100%;
    text-align: center; font-weight: 600; font-size: 21px; line-height: 25px; color: var(--ink);
  }
  .rule { position: absolute; left: 40px; width: 200px; height: 1.5px; background: var(--rule); }
  .rule--upper { top: 264px; }
  .rule--lower { top: 308px; }
  .description {
    position: absolute; top: 274px; left: 38px; width: 205px;
    font-family: "EB Garamond", serif; font-style: italic; font-size: 7.4px; line-height: 9.6px;
    text-align: justify; color: var(--body-ink);
  }

  .sea-band { position: absolute; left: 2px; right: 6px; top: 391px; height: 130px; background: var(--sea-blue); }

  .quality-seal {
    position: absolute; left: 78px; top: 326px; width: 122px; height: 122px;
    border-radius: 50%; background: var(--brand-red); border: 2px solid #fff;
  }

  .facts { position: absolute; top: 586px; width: 80px; font-size: 10px; letter-spacing: 1.2px; line-height: 14px; color: #2a2a3a; }
  .facts__rule { height: 1.5px; background: var(--rule); margin-bottom: 11px; }
  .facts--energy { left: 16px; }
  .facts--weight { left: 188px; text-align: right; }
</style>
</head>
<body>
<main class="canvas">
  <div class="pouch">
    <div class="pouch__seal pouch__seal--top"></div>
    <div class="pouch__seal pouch__seal--bottom"></div>

    <section class="label">
      <div class="brand">
        <span class="brand__dot"></span>
        <span class="brand__name">MARENJI</span>
      </div>

      <h1 class="product-name">CUT OCTOPUS,<br>TAKO SASHIMI</h1>
      <div class="rule rule--upper"></div>
      <p class="description">Lorem ipsum dolor sit amet, consectetuer elit. Cum sociis natoque penatibus et magnis dis parturient montes, nascetur ridiculus mus.</p>
      <div class="rule rule--lower"></div>

      <div class="sea-band"></div>
      <div class="quality-seal" role="img" aria-label="Round premium quality natural product seal"></div>

      <div class="facts facts--energy">
        <div class="facts__rule"></div>
        PER 100g<br>630kcal
      </div>
      <div class="facts facts--weight">
        <div class="facts__rule"></div>
        NET WT.<br>113g
      </div>
    </section>
  </div>
</main>
</body>
</html>
```